Need UI Design for HRIS/Company Employee Portal

Currently have a custom built system that we hire and use as our employee database and employee portal for everyone in our company. The software has evolved dramatically and needs to be completely user friendly and aesthetically pleasing. Attached are a few ideas and pages we already have. Please make 5 designs for the 5 different pages below. Would need all specifications of content used, color code, font/typography, icons used, etc. We can pretty much pull any information from anywhere we have for example, employee photo, address, DOB, Hire date, Title, ETC.

-Company Staff/Admin Welcome Page
- We want quick shortcuts/buttons or icons for staff functions, such as terminate, hire, information change, reports, etc
-Employee Profile Welcome Page
- We want quick shortcuts/buttons or icons for direct deposit, time off request, information change, pay stubs
-List of Applications/Candidates Page
-Profile Search Page
-Manage Inventory

Target Market(s)

Employees

Industry/Entity Type

It Company

Coding

Coded - Design and coding required

Number of Pages Required

5+ page

Font styles to use
Sans Serif

Requirements
Must have
• Must be professional! Aesthetics, Icons, Easy User Interface, Modern New technology look, can be responsive to mobile
Should not have
• Nothing old school

```html
<!DOCTYPE html>
<html lang="en">
<head>
<meta charset="utf-8">
<title>Employee Portal – Home</title>
<link href="https://fonts.googleapis.com/css2?family=Open+Sans:wght@400;600;700&display=swap" rel="stylesheet">
<style>
:root{
  --navy:#2b3285;
  --gold:#e0b32a;
  --red:#e5261e;
  --panel:#efeded;
  --field-border:#dcdcdc;
  --text:#3a3a3a;
  --muted:#9a9a9a;
  --footer:#232323;
  --white:#ffffff;
}
*{box-sizing:border-box;margin:0;padding:0}
html,body{width:1200px;height:999px;overflow:hidden}
body{font-family:"Open Sans",Arial,sans-serif;color:var(--text);background:var(--white);position:relative}

.site-header{position:absolute;left:0;top:0;width:1200px;height:136px;background:var(--white)}
.brand{position:absolute;left:59px;top:50px;display:flex;align-items:center;gap:12px}
.brand-mark{width:26px;height:26px;background:var(--navy);border-radius:50%}
.brand-name{font-size:17px;font-weight:700;color:var(--navy);letter-spacing:.5px;text-transform:uppercase}

.main-nav{position:absolute;left:0;top:136px;width:1200px;height:44px;background:var(--navy)}
.main-nav ul{list-style:none;display:flex;gap:29px;padding-left:60px;height:44px;align-items:center}
.main-nav a{color:var(--white);text-decoration:none;font-weight:700;font-size:14.5px;position:relative;display:block;line-height:44px}
.main-nav a.is-active::after{content:"";position:absolute;left:0;right:0;bottom:3px;height:3px;background:var(--gold)}

.profile-band{position:absolute;left:0;top:180px;width:1200px;height:377px;background:var(--panel)}
.photo-card{position:absolute;left:129px;top:39px;width:206px}
.photo{height:186px;background:linear-gradient(180deg,#c9ccce 0%,#a9adb0 55%,#3a3b3d 100%);border-bottom:2px solid var(--gold)}
.photo-info{height:88px;background:var(--navy);color:var(--white);text-align:center;font-size:14px;padding-top:9px;line-height:22px}
.photo-info .dot{display:inline-block;width:7px;height:7px;border-radius:50%;background:var(--gold);margin:0 4px 2px 2px}
.photo-info .years{font-weight:700;font-size:15px;margin-top:2px}

.field{position:absolute;height:36px;background:var(--white);border:1px solid var(--field-border);font-size:15px;color:var(--muted);padding:0 12px;line-height:34px}
.btn-rehire{position:absolute;left:857px;top:276px;width:95px;height:35px;background:var(--navy);color:var(--white);font-weight:700;font-size:15px;text-align:center;line-height:35px}

.panel{position:absolute;background:var(--panel);border:1px solid #e2e2e2}
.panel-head{height:41px;background:var(--navy);color:var(--white);font-weight:700;font-size:17px;line-height:41px;padding-left:9px;letter-spacing:.3px}
.panel-body{font-size:13.5px;line-height:19.5px;padding:9px 10px}

.permit-title{background:var(--white);margin:13px 6px 0;height:35px;line-height:35px;padding-left:9px;font-size:17px}
.permit-title.guard{color:var(--red)}
.permit-title.driver{color:#111;font-weight:600}
.permit-rows{display:grid;grid-template-columns:110px 1fr;column-gap:14px;row-gap:3px;font-size:14.5px;margin:18px 0 0;padding-right:10px}
.permit-rows dt{text-align:right}
.permit-rows.after{margin:17px 0 0}

.calendar{position:absolute;left:801px;top:605px;width:260px;height:276px;background:var(--white);border:2px solid #e3e3e3;border-top:none}
.calendar .panel-head{position:relative;margin:0 -2px;padding-left:11px}
.calendar .panel-head svg{position:absolute;right:8px;top:8px}
.cal-grid{display:grid;grid-template-columns:repeat(7,31px);justify-content:center;row-gap:0;margin-top:9px;text-align:center;font-size:14px;font-weight:600}
.cal-grid span{height:32px;line-height:32px}
.cal-grid .dow{color:var(--muted);font-weight:400;font-size:13px;height:24px;line-height:24px}
.cal-grid .off{color:#d3d3d3;font-size:10px}
.cal-grid .today{position:relative;color:#111}
.cal-grid .today::before{content:"";position:absolute;left:0;top:1px;width:30px;height:30px;border-radius:50%;background:var(--gold);z-index:-1}
.cal-grid .today{z-index:0}

.site-footer{position:absolute;left:0;top:957px;width:1200px;height:42px;background:var(--footer);color:#e6e6e6;font-size:13.5px;text-align:center;line-height:42px}
</style>
</head>
<body>
<header class="site-header">
  <div class="brand"><span class="brand-mark"></span><span class="brand-name">Sentinel Watch Services, Inc.</span></div>
</header>

<nav class="main-nav">
  <ul>
    <li><a class="is-active" href="#">HOME</a></li>
    <li><a href="#">PERSON LICENSES</a></li>
    <li><a href="#">FORM/REQUESTS</a></li>
    <li><a href="#">TEAM CONTACTS</a></li>
    <li><a href="#">BENEFITS</a></li>
    <li><a href="#">TRAINING</a></li>
    <li><a href="#">EQUIPMENT /HELP</a></li>
  </ul>
</nav>

<section class="profile-band">
  <div class="photo-card">
    <div class="photo" role="img" aria-label="Employee portrait photo"></div>
    <div class="photo-info">
      <div>Status : <span class="dot"></span>Active</div>
      <div>Hire Date :&nbsp; 8-1-2000</div>
      <div class="years">(17 Years)</div>
    </div>
  </div>
  <div class="field" style="left:365px;top:41px;width:459px">Name</div>
  <div class="field" style="left:365px;top:101px;width:459px">Address</div>
  <div class="field" style="left:365px;top:156px;width:219px">City</div>
  <div class="field" style="left:605px;top:156px;width:218px">Zip</div>
  <div class="field" style="left:367px;top:217px;width:219px">Phone</div>
  <div class="field" style="left:606px;top:217px;width:218px">Cell Phone</div>
  <div class="field" style="left:365px;top:276px;width:459px">Email</div>
  <div class="btn-rehire">Re-Hire</div>
</section>

<section class="panel" style="left:129px;top:605px;width:247px;height:278px">
  <div class="panel-head">CURRENT PERMITS</div>
  <div class="permit-title guard">Guard Card</div>
  <dl class="permit-rows">
    <dt>Expiring Date :</dt><dd>2-8-2016</dd>
    <dt>SSN :</dt><dd>2563</dd>
    <dt>State ID :</dt><dd>235641</dd>
  </dl>
  <div class="permit-title driver">Drivers License</div>
  <dl class="permit-rows after">
    <dt>Expiring Date :</dt><dd>2-8-2016</dd>
  </dl>
</section>

<section class="panel" style="left:465px;top:605px;width:247px;height:123px">
  <div class="panel-head">EMPLOYEE MESSAGE</div>
  <div class="panel-body">Lorem Ipsum is simply dummy text of the printing and typesetting industry.</div>
</section>

<section class="panel" style="left:468px;top:760px;width:247px;height:124px">
  <div class="panel-head">COMPANY MESSGAE</div>
  <div class="panel-body">Lorem Ipsum is simply dummy text of the printing and typesetting industry.</div>
</section>

<section class="calendar">
  <div class="panel-head">APRIL 2014
    <svg width="24" height="24" viewBox="0 0 24 24" fill="none" stroke="#fff" stroke-width="1.6" aria-hidden="true">
      <rect x="2" y="4" width="20" height="18" rx="2"/><line x1="2" y1="9" x2="22" y2="9"/>
      <line x1="7" y1="2" x2="7" y2="6"/><line x1="17" y1="2" x2="17" y2="6"/>
      <rect x="6" y="12" width="2" height="2" fill="#fff" stroke="none"/><rect x="11" y="12" width="2" height="2" fill="#fff" stroke="none"/><rect x="16" y="12" width="2" height="2" fill="#fff" stroke="none"/>
      <rect x="6" y="16" width="2" height="2" fill="#fff" stroke="none"/><rect x="11" y="16" width="2" height="2" fill="#fff" stroke="none"/>
    </svg>
  </div>
  <div class="cal-grid">
    <span class="dow">S</span><span class="dow">M</span><span class="dow">T</span><span class="dow">W</span><span class="dow">T</span><span class="dow">F</span><span class="dow">S</span>
    <span class="off">●</span><span class="off">●</span><span>1</span><span>2</span><span>3</span><span>4</span><span>5</span>
    <span>6</span><span>7</span><span class="today">8</span><span>9</span><span>10</span><span>11</span><span>12</span>
    <span>13</span><span>14</span><span>15</span><span>16</span><span>17</span><span>18</span><span>19</span>
    <span>20</span><span>22</span><span>23</span><span>24</span><span>25</span><span>26</span><span>27</span>
    <span>28</span><span>29</span><span>30</span><span>31</span><span class="off">●</span><span class="off">●</span><span class="off">●</span>
    <span class="off">●</span><span class="off">●</span><span class="off">●</span><span class="off">●</span><span class="off">●</span><span class="off">●</span><span class="off">●</span>
  </div>
</section>

<footer class="site-footer">Copyright © 2016 Sentinel Watch Services&nbsp; All rights reserved</footer>
</body>
</html>
```